IT Company needs stationary design

Business cards, MS Word, PowerPoint, A4 notepad design base on our company logo. This must be a set of templates in the same style which could be used both for printable documents as well as for documents shared digitally via email, website etc. This should be a modern design which is still professional, so make sure content is well readable both in MS Word and MS PowerPoint templates.

Target Market(s)

SME and Corporate

Industry/Entity Type

It Company

Font styles to use
Sans Serif

Colors
0455a3
0692cd
f37122
ffc214

Requirements
Must have
• 1) Business cards design: modern but still professional
• 2) MS Word: mostly for IT project documents (business analysis, reports, specifications, etc.) must be professional and easy readable.
• 3) MS PowerPoint: first slide, normal slide, last slide.
• 4) A4 notepad: header (must), footer (must), some light design on the background (optionally)
Nice to have
• Business cards design: would be nice to have 2-4 color variations of the same design from one side - cover (for example part of the cards are blue, part of the cards are orange) and other side with contact details is identical.

```html
<!DOCTYPE html>
<html lang="en">
<head>
<meta charset="utf-8">
<title>Corvanta – Business Card</title>
<link rel="stylesheet" href="https://fonts.googleapis.com/css2?family=Quicksand:wght@400;500&display=swap">
<style>
  :root {
    --page-bg: #e7e5e2;
    --frost-light: #eeeeee;
    --frost-mid: #d6d6d6;
    --card-dark: #141414;
    --card-dark-edge: #2a2a2a;
    --ink-dark: #3a3a3a;
    --ink-light: #e6e6e6;
    --ink-soft: #bdbdbd;
    --band-warm: #f37122;
    --band-cool: #0692cd;
  }
  html, body {
    margin: 0;
    width: 1200px;
    height: 969px;
    overflow: hidden;
    background: var(--page-bg);
  }
  .canvas {
    position: relative;
    width: 1200px;
    height: 969px;
  }
  .business-card {
    position: absolute;
    left: 100px;
    top: 198px;
    width: 1000px;
    height: 572px;
    filter: drop-shadow(0 12px 24px rgba(0,0,0,0.18));
  }
  .card-text {
    font-family: "Quicksand", sans-serif;
  }
  .brand-name { fill: var(--ink-dark); font-size: 34px; font-weight: 400; }
  .person-name { fill: var(--ink-light); font-size: 19.5px; font-weight: 400; letter-spacing: 0.5px; }
  .person-role { fill: var(--ink-soft); font-size: 13px; font-weight: 400; letter-spacing: 0.3px; }
  .contact-line { fill: var(--ink-soft); font-size: 12.5px; font-weight: 400; }
  .contact-icon { fill: var(--ink-soft); }
  .contact-icon-stroke { fill: none; stroke: var(--ink-soft); stroke-width: 1.2; }
</style>
</head>
<body>
<main class="canvas">
  <svg class="business-card" viewBox="0 0 580 332" xmlns="http://www.w3.org/2000/svg" aria-label="Corvanta business card for Dana Whitlow">
    <defs>
      <linearGradient id="frost" x1="0" y1="0" x2="1" y2="1">
        <stop offset="0" stop-color="var(--frost-light)"/>
        <stop offset="1" stop-color="var(--frost-mid)"/>
      </linearGradient>
      <linearGradient id="dark-panel" x1="0" y1="0" x2="0" y2="1">
        <stop offset="0" stop-color="var(--card-dark-edge)"/>
        <stop offset="1" stop-color="var(--card-dark)"/>
      </linearGradient>
      <linearGradient id="band-tone" x1="0" y1="0" x2="1" y2="0">
        <stop offset="0" stop-color="var(--band-warm)"/>
        <stop offset="1" stop-color="var(--band-cool)"/>
      </linearGradient>
      <clipPath id="card-shape">
        <rect x="0" y="0" width="580" height="332" rx="12"/>
      </clipPath>
    </defs>

    <g clip-path="url(#card-shape)">
      <rect class="card-face" x="0" y="0" width="580" height="332" fill="url(#frost)"/>

      <path class="accent-band" role="img" aria-label="Decorative coloured wave band"
            d="M-10,258 C120,300 200,262 280,182 C340,122 420,82 500,80 C540,80 570,90 590,100 L590,124 C570,114 540,104 500,104 C420,106 340,144 280,204 C200,284 120,322 -10,280 Z"
            fill="url(#band-tone)" opacity="0.85"/>

      <path class="contact-panel" d="M-10,280 C120,322 200,284 280,204 C340,144 420,106 500,104 C540,104 570,114 590,124 L590,340 L-10,340 Z" fill="url(#dark-panel)"/>
    </g>

    <g class="brand">
      <circle cx="57" cy="87" r="21" fill="none" stroke="var(--ink-dark)" stroke-width="3"/>
      <text class="card-text brand-name" x="92" y="98">corvanta</text>
    </g>

    <g class="card-text" text-anchor="end">
      <text class="person-name" x="548" y="156">DANA WHITLOW</text>
      <text class="person-role" x="548" y="175">CEO/FOUNDER</text>

      <text class="contact-line" x="527" y="206">555 210 4471</text>
      <text class="contact-line" x="527" y="225">555 382 0196</text>
      <text class="contact-line" x="527" y="244">dana@corvanta.com</text>
      <text class="contact-line" x="527" y="263">www.corvanta.com</text>

      <text class="contact-line" x="548" y="288">4418 Juniper Lane</text>
      <text class="contact-line" x="548" y="307">Fairview, Oregon 97024</text>
    </g>

    <g class="contact-icons">
      <path class="contact-icon" d="M537,198 c1,-1 2,-1 2.5,0 l1.5,2.5 c0.4,0.8 0,1.4 -0.7,1.9 c0.6,1.6 1.6,2.6 3.2,3.2 c0.5,-0.7 1.1,-1.1 1.9,-0.7 l2.5,1.5 c1,0.5 1,1.5 0,2.5 c-1.5,1.4 -4,1 -7,-2 c-3,-3 -3.4,-5.5 -2,-7 z"/>
      <rect class="contact-icon-stroke" x="539.5" y="215" width="6" height="11" rx="1"/>
      <rect class="contact-icon" x="541.5" y="223.5" width="2" height="1"/>
      <rect class="contact-icon" x="537" y="235.5" width="11" height="8" rx="0.8"/>
      <path d="M537.5,236.5 L542.5,240.5 L547.5,236.5" fill="none" stroke="var(--card-dark)" stroke-width="1"/>
      <circle class="contact-icon-stroke" cx="542.5" cy="259" r="5"/>
      <path class="contact-icon-stroke" d="M537.5,259 h10 M542.5,254 c-2.5,3 -2.5,7 0,10 c2.5,-3 2.5,-7 0,-10"/>
    </g>
  </svg>
</main>
</body>
</html>
```